Clinc flyer

We need a flyer for our Physiotherapy and Acupuncture clinic to leave in a gym.
It needs the clinc logo and also:
"Free physiotherapy and acupuncture treament with an LPB claim." This should be larger text
"No referral needed" This should be under the previous text
"271c Tarevo Mall (entry via Brindle St)"
"582 3910"

```html
<!DOCTYPE html>
<html lang="en">
<head>
<meta charset="utf-8">
<title>Kinetic Restore – Clinic Flyer</title>
<link href="https://fonts.googleapis.com/css2?family=Fira+Sans:ital,wght@0,500;0,600;1,500&family=Montserrat:wght@400;500;700&display=swap" rel="stylesheet">
<style>
  :root {
    --backdrop: #7b7b7b;
    --paper: #ffffff;
    --sky: #0aaedf;
    --teal: #117a93;
    --teal-deep: #0f6f86;
    --ink: #1e2326;
    --body-grey: #6b7074;
    --icon-bg: #e4e7e9;
  }
  html, body {
    margin: 0;
    width: 1200px;
    height: 1200px;
    overflow: hidden;
    background: var(--backdrop);
  }
  .flyer {
    position: absolute;
    left: 137px;
    top: 0;
    width: 925px;
    height: 1200px;
    background: var(--paper);
  }
  .flyer svg { display: block; }
  .brand-name { font-family: "Fira Sans", sans-serif; font-weight: 600; fill: var(--teal); }
  .brand-tag { font-family: "Montserrat", sans-serif; font-weight: 500; fill: var(--teal); letter-spacing: 5px; }
  .headline { font-family: "Fira Sans", sans-serif; font-weight: 600; fill: var(--sky); }
  .headline-sub { font-family: "Fira Sans", sans-serif; font-style: italic; font-weight: 500; fill: var(--teal); }
  .badge-text { font-family: "Montserrat", sans-serif; font-weight: 700; fill: #fff; }
  .intro { font-family: "Montserrat", sans-serif; font-weight: 400; fill: var(--body-grey); font-size: 15px; }
  .condition { font-family: "Montserrat", sans-serif; font-weight: 500; fill: var(--ink); font-size: 15px; }
  .condition-icon { fill: var(--icon-bg); }
  .condition-dot { fill: var(--teal); }
  .contact { font-family: "Montserrat", sans-serif; fill: #fff; }
</style>
</head>
<body>
<div class="flyer">
<svg width="925" height="1200" viewBox="0 0 925 1200" xmlns="http://www.w3.org/2000/svg">
  <defs>
    <linearGradient id="treatment-tone" x1="0" y1="0" x2="1" y2="1">
      <stop offset="0" stop-color="#d9d9d9"/>
      <stop offset="0.55" stop-color="#8c8c8c"/>
      <stop offset="0.8" stop-color="#e2646a"/>
      <stop offset="1" stop-color="#bdbdbd"/>
    </linearGradient>
    <radialGradient id="needle-tone" cx="0.4" cy="0.45" r="0.7">
      <stop offset="0" stop-color="#e9b7a6"/>
      <stop offset="0.6" stop-color="#c98f80"/>
      <stop offset="1" stop-color="#2a2526"/>
    </radialGradient>
  </defs>

  <!-- Header brand -->
  <g class="brand">
    <circle cx="88" cy="90" r="32" fill="var(--teal)"/>
    <text class="brand-name" x="142" y="106" font-size="46">Kinetic Restore</text>
    <text class="brand-tag" x="144" y="126" font-size="12">ACUPUNCTURE PHYSIOTHERAPY</text>
  </g>

  <!-- Treatment photo area -->
  <path role="img" aria-label="Black and white photo of a physiotherapist's hands massaging a knee, highlighted red"
        d="M0,200 C280,210 640,168 925,10 L925,460 C760,520 640,545 560,545 C350,545 150,500 0,450 Z"
        fill="url(#treatment-tone)"/>

  <!-- Top wave band -->
  <path d="M0,152 C260,178 640,150 925,0 L925,16 C640,176 280,214 0,208 Z" fill="var(--sky)"/>

  <!-- Lower wave band under photo -->
  <path d="M0,446 C150,498 350,540 560,540 C680,540 800,500 925,452 L925,486 C800,520 680,552 560,552 C350,552 150,520 0,455 Z" fill="var(--sky)"/>

  <!-- No referral badge -->
  <g class="badge">
    <circle cx="762" cy="513" r="94" fill="#fff"/>
    <circle cx="762" cy="513" r="83" fill="var(--teal)"/>
    <text class="badge-text" x="762" y="509" font-size="52" text-anchor="middle">NO</text>
    <text class="badge-text" x="762" y="538" font-size="25" text-anchor="middle">REFERRAL</text>
    <text class="badge-text" x="762" y="563" font-size="25" text-anchor="middle">NEEDED</text>
  </g>

  <!-- Headline -->
  <rect x="56" y="567" width="13" height="138" fill="var(--teal)"/>
  <text class="headline" x="88" y="611" font-size="55">FREE PHYSIOTHERAPY</text>
  <text class="headline" x="88" y="667" font-size="55">AND ACUPUNCTURE TREAMENT</text>
  <text class="headline-sub" x="88" y="706" font-size="37">with an LPB claim</text>

  <!-- Intro copy -->
  <text class="intro" x="55" y="734">We have a wide range of products available for purchase ranging from strapping products, massage waxes</text>
  <text class="intro" x="55" y="754">and crèmes, ice packs, wheat bags, exercise &amp; rehabilitation products. We deal with a variety of suppliers to</text>
  <text class="intro" x="55" y="774">ensure that we are able bring top quality products at the most competitive prices possible.</text>

  <!-- Conditions grid -->
  <g class="conditions">
    <g><circle class="condition-icon" cx="78" cy="820" r="23"/><circle class="condition-dot" cx="78" cy="820" r="7"/>
      <text class="condition" x="112" y="816">CHRONIC</text><text class="condition" x="112" y="834">PAIN</text></g>
    <g><circle class="condition-icon" cx="286" cy="820" r="23"/><circle class="condition-dot" cx="286" cy="820" r="7"/>
      <text class="condition" x="320" y="826">OSTEOPOROSIS</text></g>
    <g><circle class="condition-icon" cx="501" cy="820" r="23"/><circle class="condition-dot" cx="501" cy="820" r="7"/>
      <text class="condition" x="536" y="826">KNEE PAIN</text></g>
    <g><circle class="condition-icon" cx="709" cy="820" r="23"/><circle class="condition-dot" cx="709" cy="820" r="7"/>
      <text class="condition" x="744" y="826">HEEL PAIN</text></g>

    <g><circle class="condition-icon" cx="78" cy="878" r="23"/><circle class="condition-dot" cx="78" cy="878" r="7"/>
      <text class="condition" x="112" y="875">LIVING AFTER</text><text class="condition" x="112" y="893">A STROKE</text></g>
    <g><circle class="condition-icon" cx="286" cy="878" r="23"/><circle class="condition-dot" cx="286" cy="878" r="7"/>
      <text class="condition" x="320" y="875">LOWER BACK</text><text class="condition" x="320" y="893">PAIN</text></g>
    <g><circle class="condition-icon" cx="501" cy="878" r="23"/><circle class="condition-dot" cx="501" cy="878" r="7"/>
      <text class="condition" x="536" y="875">RHEUMATOID</text><text class="condition" x="536" y="893">ARTHRITIS</text></g>
    <g><circle class="condition-icon" cx="709" cy="878" r="23"/><circle class="condition-dot" cx="709" cy="878" r="7"/>
      <text class="condition" x="744" y="875">ADVANCED</text><text class="condition" x="744" y="893">ACUPUNCTURE</text></g>

    <g><circle class="condition-icon" cx="78" cy="943" r="23"/><circle class="condition-dot" cx="78" cy="943" r="7"/>
      <text class="condition" x="112" y="940">ANKLE</text><text class="condition" x="112" y="958">PAIN</text></g>
    <g><circle class="condition-icon" cx="286" cy="943" r="23"/><circle class="condition-dot" cx="286" cy="943" r="7"/>
      <text class="condition" x="320" y="949">PARKINSON’S</text></g>
    <g><circle class="condition-icon" cx="501" cy="943" r="23"/><circle class="condition-dot" cx="501" cy="943" r="7"/>
      <text class="condition" x="536" y="937">TENNIS</text><text class="condition" x="536" y="955">ELBOW</text></g>

    <g><circle class="condition-icon" cx="78" cy="1004" r="23"/><circle class="condition-dot" cx="78" cy="1004" r="7"/>
      <text class="condition" x="112" y="1010">NECK PAIN</text></g>
    <g><circle class="condition-icon" cx="286" cy="1004" r="23"/><circle class="condition-dot" cx="286" cy="1004" r="7"/>
      <text class="condition" x="320" y="999">SPORTS</text><text class="condition" x="320" y="1017">INJURIES</text></g>
    <g><circle class="condition-icon" cx="501" cy="1004" r="23"/><circle class="condition-dot" cx="501" cy="1004" r="7"/>
      <text class="condition" x="536" y="999">REPETITIVE</text><text class="condition" x="536" y="1017">STRAIN INJURY</text></g>
  </g>

  <!-- Footer band -->
  <path d="M0,1080 C180,1048 420,1036 620,1052 C740,1062 840,1100 925,1150 L925,1200 L0,1200 Z" fill="var(--sky)"/>
  <path d="M0,1080 C180,1048 420,1036 620,1052 L620,1055 C420,1042 180,1056 0,1090 Z" fill="var(--teal-deep)"/>

  <!-- Contact details -->
  <g class="contact-block">
    <circle cx="63" cy="1089" r="8" fill="none" stroke="#fff" stroke-width="1.6"/>
    <path d="M59,1092 L59,1088 L63,1084 L67,1088 L67,1092 Z" fill="#fff"/>
    <text class="contact" x="80" y="1096" font-size="17">271c Tarevo Mall</text>
    <text class="contact" x="80" y="1119" font-size="13.5">(corner of Alder Street and Brindle</text>
    <text class="contact" x="80" y="1141" font-size="13.5">Street). Tarevo.</text>

    <circle cx="396" cy="1089" r="8.5" fill="none" stroke="#fff" stroke-width="1.6"/>
    <path d="M392,1084 q-1,6 4,10 l2,-2 l-2,-2 l-1,1 q-2,-2 -2,-4 l1,-1 l-1,-3 Z" fill="#fff"/>
    <text class="contact" x="410" y="1096" font-size="17" font-weight="700">(09) 582 3910</text>

    <circle cx="396" cy="1123" r="8.5" fill="none" stroke="#fff" stroke-width="1.6"/>
    <rect x="391" y="1119" width="10" height="7" fill="none" stroke="#fff" stroke-width="1.2"/>
    <text class="contact" x="410" y="1130" font-size="17">hello@kineticrestore.nz</text>
  </g>

  <!-- Acupuncture photo circle -->
  <circle cx="782" cy="1060" r="124" fill="#cfcfcf"/>
  <circle cx="782" cy="1060" r="121" fill="#fff"/>
  <circle role="img" aria-label="Close-up photo of fingers placing an acupuncture needle into skin" cx="784" cy="1062" r="110" fill="url(#needle-tone)"/>
</svg>
</div>
</body>
</html>
```